Market Cross Chapel needs an eye-catching, evocative & inviting poster

We need a poster to 'advertise' what we are about. We are an Anglican church on the main town square of Bramford, Surrey UK. We offer a variety of services although all fairly informal.

The poster should ideally ILLUSTRATE the following words, which in turn need to feature boldly on the poster:

Meeting friends
Enjoying God
Living life better.

In SMALLER type it needs our contact details
[twitter logo] @mcbramford
marketcrosschapelbramford.org
01632 958214

Also main services times [again in SMALLER TYPE]:

8am Holy Communion (contemplative)
9.15 & 11am All-age worship (informal with children's programme)
7pm Informal worship (modern & contemporary)

You can find out more about us from our website: www.marketcrosschapelbramford.org

I am uploading a 'logo' - the blue background ISN'T essential, but the 'MarketCross Bramford' part should ideally feature in the poster.
Updates

Hi all

Thanks for the designs so far.  I am looking for something that is more evocative than most that have been submitted.

The words "Meeting friends" etc are the most important.  The MarketCross Bramford words, are of secondary importance and should reflect that, and the contact details are for people who will, having seen the poster, will make the effort to get the details.  

Target Market(s)

Passers-by

Industry/Entity Type

Church

```html
<!DOCTYPE html>
<html lang="en">
<head>
<meta charset="utf-8">
<title>MarketCross Bramford – Poster</title>
<link rel="stylesheet" href="https://fonts.googleapis.com/css2?family=Abril+Fatface&family=PT+Sans:wght@700&family=Didact+Gothic&display=swap">
<style>
  :root {
    --top-band: #7af7ec;
    --logo-band-top: #4f8ff2;
    --logo-band-bottom: #6fc6f2;
    --deep-blue: #0a2fc4;
    --mid-blue: #1d6ff0;
    --light-blue: #9fe4ff;
    --teal-glow: #4fe3d0;
    --bullet: #7ff5ec;
    --white: #ffffff;
  }
  * { margin: 0; padding: 0; box-sizing: border-box; }
  html, body { width: 811px; height: 1200px; overflow: hidden; background: var(--deep-blue); }
  .poster { position: relative; width: 811px; height: 1200px; overflow: hidden; }
  .top-band { position: absolute; left: 0; top: 0; width: 100%; height: 65px; background: var(--top-band); }
  .logo-band {
    position: absolute; left: 0; top: 65px; width: 100%; height: 266px;
    background: linear-gradient(180deg, var(--logo-band-top) 0%, var(--logo-band-bottom) 100%);
  }
  .church-name {
    position: absolute; left: 88px; top: 140px; width: 574px;
    font-family: "PT Sans", sans-serif; font-weight: 700; color: var(--white);
    line-height: 1;
  }
  .church-name .primary { display: block; font-size: 110px; letter-spacing: -1px; white-space: nowrap; }
  .church-name .town { display: block; text-align: right; font-size: 50px; margin-top: -8px; }
  .light-burst {
    position: absolute; left: 0; top: 331px; width: 100%; height: 869px;
    background:
      radial-gradient(ellipse 60% 40% at 80% 35%, rgba(220,245,255,0.85) 0%, rgba(159,228,255,0.4) 40%, rgba(159,228,255,0) 75%),
      radial-gradient(ellipse 55% 35% at 85% 95%, rgba(79,227,208,0.6) 0%, rgba(79,227,208,0) 70%),
      linear-gradient(160deg, var(--deep-blue) 0%, var(--mid-blue) 40%, #3fa6f5 65%, #1e63d8 85%, #0b2a8a 100%);
  }
  .headline {
    position: absolute; left: 86px; top: 428px;
    font-family: "Abril Fatface", serif; font-weight: 400; font-size: 70px; line-height: 85px;
    color: var(--white); letter-spacing: 5px; white-space: nowrap;
  }
  .services {
    position: absolute; left: 59px; top: 786px; list-style: none;
    font-family: "Didact Gothic", sans-serif; font-size: 30px; line-height: 35px; color: var(--white);
    white-space: nowrap;
  }
  .services li { position: relative; padding-left: 49px; }
  .services li::before {
    content: ""; position: absolute; left: 0; top: 4px; width: 28px; height: 28px;
    border-radius: 50%; background: var(--bullet);
  }
  .contact {
    position: absolute; left: 105px; top: 1073px;
    font-family: "Didact Gothic", sans-serif; font-size: 26px; line-height: 31px; color: var(--white);
  }
  .contact .social { display: flex; align-items: center; gap: 10px; }
  .contact .social-dot { width: 16px; height: 16px; border-radius: 50%; background: var(--bullet); }
</style>
</head>
<body>
  <div class="poster">
    <div class="top-band"></div>
    <div class="logo-band"></div>
    <div class="church-name">
      <span class="primary">MarketCross</span>
      <span class="town">Bramford</span>
    </div>
    <div class="light-burst" role="img" aria-label="Abstract streaks of blue and teal light bursting across a starry background"></div>
    <h1 class="headline">Meeting friends<br>Enjoying God<br>Living life better</h1>
    <ul class="services">
      <li>8am Holy Communion<br>(contemplative)</li>
      <li>9.15 &amp; 11am All-age worship<br>&nbsp;(informal with children's programme)</li>
      <li>7pm Informal worship (modern &amp; contemporary)</li>
    </ul>
    <div class="contact">
      <p class="social"><span class="social-dot"></span>@mcbramford</p>
      <p>marketcrosschapelbramford.org</p>
      <p>01632 958214</p>
    </div>
  </div>
</body>
</html>
```